Etiketten für Dips
Zielgruppe
Landwirtschaft mit Direktvermarktung und Diversifikation durch workshops und Beratung zur Selbstversorgung
Zielgruppe: LOHAS, Best Agers
Aufgabenstellung
es gibt pikante und süße Dips (Weiters Salz und Essig) unter dem Motto 'Würzen | Dippen | Toppen' (das soll unbedingt überall mit drauf aufs Etikett), Etikett passend zum Logo - möglicherweise Teile davon auch am Etikett? durchscheinend aber farbig? die Etiketten jeweils in unterschiedlichen 'Farbmotto' so dass eine bunte aber gediegene Serie mit Wiedererkennung entstehen die höheres Preissegment gerecht wird/unterstreicht. Etikett soll nur 1 Teil sein, da am Deckel der Gläser ohnehin das Logoetikett drauf kommt. Bei Siegerprojekt gerne weitere Zusammenarbeit für die weiteren Etiketten.
Produkte für die Etiketten benötigt werden: Mara Bunt (Tomaten-Dip), Brisa Paul (Salz mit Tomaten), Sommer-Rübli (Grillsauce/-dip), Moosgeflüster (Lebkuchenmarmelade), Wild Mango, Kornbrise (Gewürzessig mit Chilli)
Bitte an alle notwendigen Inhalte eines Lebensmitteletiketts denken bzw Platzhalter einfügen

```html
<!DOCTYPE html>
<html lang="de">
<head>
<meta charset="utf-8">
<title>Mara Bunt – Etikett</title>
<link rel="stylesheet" href="https://fonts.googleapis.com/css2?family=Montserrat:wght@400;500;600&family=Playfair+Display:wght@700&display=swap">
<style>
  :root {
    --label-red: #b3272b;
    --ink: #1a1a1a;
    --paper: #ffffff;
    --rule: #c0393b;
  }
  * { margin: 0; padding: 0; box-sizing: border-box; }
  html, body { width: 1200px; height: 900px; overflow: hidden; background: var(--paper); }
  .label {
    position: relative; width: 1200px; height: 900px; overflow: hidden;
    background: var(--paper);
    font-family: "Montserrat", Arial, sans-serif;
    color: var(--ink);
  }
  .edge { position: absolute; top: 0; bottom: 0; width: 20px; background: var(--label-red); }
  .edge--left { left: 0; }
  .edge--right { right: 0; }

  .brand {
    position: absolute; top: 100px; right: 72px;
    display: flex; align-items: center; gap: 14px;
    font-size: 36px; font-weight: 500; color: var(--label-red);
  }
  .brand-dot { width: 26px; height: 26px; border-radius: 50%; background: var(--label-red); }

  .product-name {
    position: absolute; left: 60px; top: 222px;
    font-family: "Playfair Display", Georgia, serif;
    font-weight: 700; font-size: 178px; line-height: 1;
    color: var(--label-red); letter-spacing: -1px; white-space: nowrap;
  }
  .rule { position: absolute; left: 64px; width: 1061px; height: 2px; background: var(--rule); }
  .rule--title { top: 436px; }
  .rule--info-top { top: 540px; }
  .rule--info-bottom { top: 636px; }

  .motto {
    position: absolute; left: 66px; top: 452px;
    font-size: 56px; font-weight: 400; word-spacing: 12px; white-space: nowrap;
  }

  .storage {
    position: absolute; left: 64px; top: 556px; width: 760px;
    font-size: 26px; font-weight: 600; line-height: 32px; color: var(--label-red);
  }
  .info-divider { position: absolute; left: 859px; top: 540px; width: 2px; height: 96px; background: var(--rule); }
  .net-weight {
    position: absolute; left: 861px; width: 264px; top: 542px; height: 94px;
    display: flex; align-items: center; justify-content: center;
    font-size: 52px; font-weight: 500; color: var(--label-red);
  }

  .ingredients { position: absolute; left: 64px; top: 648px; display: flex; }
  .ingredients-label { font-size: 36px; font-weight: 500; line-height: 38px; width: 158px; white-space: nowrap; }
  .ingredients-list { font-size: 28px; line-height: 31px; padding-top: 5px; width: 915px; }

  .imprint {
    position: absolute; left: 73px; top: 804px; width: 1054px;
    display: flex; align-items: center;
    font-size: 22px; font-weight: 500; color: var(--label-red); white-space: nowrap;
  }
  .imprint-item { padding: 0 16px; border-left: 2px solid var(--rule); line-height: 36px; }
  .imprint-item:first-child { padding-left: 0; border-left: none; }
</style>
</head>
<body>
  <main class="label">
    <div class="edge edge--left"></div>
    <div class="edge edge--right"></div>

    <div class="brand"><span class="brand-dot"></span><span class="brand-name">Beetwerk</span></div>

    <h1 class="product-name">Mara Bunt</h1>
    <div class="rule rule--title"></div>

    <p class="motto">Würzen Dippen Toppen</p>

    <div class="rule rule--info-top"></div>
    <p class="storage">Nach dem Öffnen kühl lagern, nach dem Öffnen innerhalb von einer Woche genießen.</p>
    <div class="info-divider"></div>
    <p class="net-weight">180 g</p>
    <div class="rule rule--info-bottom"></div>

    <div class="ingredients">
      <span class="ingredients-label">Zutaten:</span>
      <p class="ingredients-list">96 % Tomaten, Zwiebel, Knoblauch, Stangensellerie, Senfkörner, Bio Apfelessig, Bio Gellerzucker, Bio Gewürze</p>
    </div>

    <footer class="imprint">
      <span class="imprint-item">BEETWERK HOF</span>
      <span class="imprint-item">Au 14, 3571, Lindtal</span>
      <span class="imprint-item">+43 660 12 34 578</span>
      <span class="imprint-item">hallo@beetwerk.at</span>
    </footer>
  </main>
</body>
</html>
```